Business Card for Language School (2 locations)

We need a sleek business card for a language school that is looking to update our image to be more professional. We work with students ages Pre-Kindergarten through adults. Our idea is to have an all-black business card with white or silver lettering. On the front will be the name of our school (Bright Maple English Academy), and on the back there will be information for our location, phone number, email, and website (and possibly social media information). We have two school branches, so the address, phone number, and email address will be different for each branch, but all of the other information will stay the same. We'd like each branch to have a different color card edge that is neon. We are also open to suggestions and new ideas!

Some answers to questions we have received:
1. The reason we haven't added a logo is because we are looking to get a new one. We hadn't originally planned to do that at this time, but we are going to look into updating our project to include that as another aspect of it. We had previously planned to just include the school name on the front without a logo at this time.
2. We currently have two branches of our school, and we want our business card design to be uniform for each location. While it might make sense to put the information on one card right now, we plan to have more locations in the future, so we want to plan ahead with a unified design right now.
3. Our school addresses and phone numbers can be found on our website: www.brightmapleenglish.example (at the bottom of the page)!
Updates

Part of this contest is also a new logo design. Our previous design was a train, which we would be open to keeping if it had an updated, sleeker design.

Contact Information for Business Card

Card #1:
Bright Maple English Academy (Qiaolin Branch)
Yuqing W. Rd. Sec. 3, Lane 412, No. 29, 1F
Beitou District, Taipei City 11268
02-2649-3058
qiaolin@brightmapleenglish.example

Card #2:
Bright Maple English Academy (Fenghe Branch)
Fulan Road, No. 318, 1F
Songshan District, Taipei City 10573
02-2761-4402
fenghe@brightmapleenglish.example

Both cards:
Website: www.brightmapleenglish.example
Facebook: www.facebook.com/brightmapleenglish
Instagram: @brightmapleenglish

```html
<!DOCTYPE html>
<html lang="en">
<head>
<meta charset="utf-8">
<title>Bright Maple English Academy — Business Card</title>
<link href="https://fonts.googleapis.com/css2?family=Overpass:wght@700;800&display=swap" rel="stylesheet">
<style>
  :root {
    --page: #ffffff;
    --card: #000000;
    --ink: #ffffff;
    --neon: #0a6cff;
    --neon-glow: rgba(30, 120, 255, 0.75);
  }
  * { box-sizing: border-box; margin: 0; padding: 0; }
  html, body {
    width: 1200px; height: 1200px; overflow: hidden;
    background: var(--page);
    font-family: "Overpass", Arial, sans-serif;
    color: var(--ink);
  }
  .card {
    position: absolute; left: 204px; width: 792px; height: 484px;
    background: var(--card);
    box-shadow: 6px 6px 8px rgba(0,0,0,0.45);
    overflow: visible;
  }
  .card--front { top: 66px; }
  .card--back { top: 672px; }

  .neon-bar {
    position: absolute; background: var(--neon);
    box-shadow: 0 0 8px 2px var(--neon-glow);
  }
  .neon-bar--upper { left: 155px; top: 0; width: 19px; height: 194px; }
  .neon-bar--lower { left: 155px; top: 428px; width: 19px; height: 56px; }
  .neon-bar--band { left: 0; top: 410px; width: 792px; height: 11px; }

  .front-wordmark {
    position: absolute; left: 42px; top: 52px; width: 100px;
    font-weight: 800; font-size: 17px; line-height: 1.15;
    color: var(--ink);
  }
  .school-name {
    position: absolute; left: 232px; top: 38px;
    font-weight: 800; font-size: 32px; letter-spacing: 0.3px; white-space: nowrap;
  }
  .branch-name {
    position: absolute; left: 232px; top: 78px;
    font-weight: 700; font-size: 22px; letter-spacing: 0.3px;
  }
  .contact-icon {
    position: absolute; left: 151px; width: 28px; height: 28px;
  }
  .contact-text {
    position: absolute; left: 232px;
    font-weight: 700; font-size: 14px; line-height: 21px; white-space: nowrap;
  }

  .back-wordmark {
    position: absolute; left: 0; width: 792px; top: 176px;
    text-align: center; font-weight: 800; color: var(--ink);
  }
  .back-wordmark__top { font-size: 22px; letter-spacing: 3px; line-height: 1.3; }
  .back-wordmark__main { font-size: 37px; letter-spacing: 2px; line-height: 1.15; }

  .social {
    position: absolute; top: 440px; height: 28px;
    display: flex; align-items: center; gap: 35px;
    font-weight: 700; font-size: 14.5px; letter-spacing: 0.3px;
  }
  .social__dot {
    width: 28px; height: 28px; border-radius: 50%; background: var(--neon);
  }
  .social--facebook { left: 181px; }
  .social--instagram { left: 424px; }
</style>
</head>
<body>

<section class="card card--front">
  <div class="neon-bar neon-bar--upper"></div>
  <div class="neon-bar neon-bar--lower"></div>

  <div class="front-wordmark">Bright Maple</div>

  <h1 class="school-name">Bright Maple English Academy</h1>
  <h2 class="branch-name">Qiaolin Branch</h2>

  <svg class="contact-icon" style="top:218px" viewBox="0 0 28 28" aria-hidden="true">
    <circle cx="14" cy="14" r="14" fill="var(--neon)"/>
    <path d="M14 6.5a5 5 0 0 0-5 5c0 3.8 5 9.5 5 9.5s5-5.7 5-9.5a5 5 0 0 0-5-5z" fill="#fff"/>
    <circle cx="14" cy="11.5" r="2" fill="var(--neon)"/>
  </svg>
  <p class="contact-text" style="top:212px">Yuqing W. Rd. Sec. 3, Lane 412, No. 29, 1F<br>Beitou District, Taipei City 11268</p>

  <svg class="contact-icon" style="top:270px" viewBox="0 0 28 28" aria-hidden="true">
    <circle cx="14" cy="14" r="14" fill="var(--neon)"/>
    <path d="M9.5 7.5l2.5-.3 1.3 3.3-1.6 1.2a8 8 0 0 0 4.4 4.4l1.2-1.6 3.3 1.3-.3 2.5c-.2 1.1-1.3 1.7-2.4 1.5C12.5 19 9 15.5 8 10.9c-.2-1.1.4-2.2 1.5-3.4z" fill="#fff"/>
    <path d="M16 8a4.5 4.5 0 0 1 4 4M16 5.5a7 7 0 0 1 6.5 6.5" stroke="#fff" stroke-width="1.3" fill="none" stroke-linecap="round"/>
  </svg>
  <p class="contact-text" style="top:274px">02-2649-3058</p>

  <svg class="contact-icon" style="top:322px" viewBox="0 0 28 28" aria-hidden="true">
    <circle cx="14" cy="14" r="14" fill="var(--neon)"/>
    <rect x="7.5" y="9.5" width="13" height="9" rx="1" fill="#fff"/>
    <path d="M7.8 10l6.2 5 6.2-5" stroke="var(--neon)" stroke-width="1.2" fill="none"/>
  </svg>
  <p class="contact-text" style="top:325px">qiaolin@brightmapleenglish.example</p>

  <svg class="contact-icon" style="top:374px" viewBox="0 0 28 28" aria-hidden="true">
    <circle cx="14" cy="14" r="14" fill="var(--neon)"/>
    <g stroke="#fff" stroke-width="1.2" fill="none">
      <circle cx="14" cy="14" r="7"/>
      <ellipse cx="14" cy="14" rx="3" ry="7"/>
      <path d="M7 14h14M8 10.5h12M8 17.5h12"/>
    </g>
  </svg>
  <p class="contact-text" style="top:377px">www.brightmapleenglish.example</p>
</section>

<section class="card card--back">
  <div class="back-wordmark">
    <div class="back-wordmark__top">BRIGHT MAPLE ENGLISH</div>
    <div class="back-wordmark__main">ACADEMY</div>
  </div>

  <div class="neon-bar neon-bar--band"></div>

  <div class="social social--facebook">
    <span class="social__dot"></span>
    <span class="social__handle">brightmapleenglish</span>
  </div>
  <div class="social social--instagram">
    <span class="social__dot"></span>
    <span class="social__handle">@brightmapleenglish</span>
  </div>
</section>

</body>
</html>
```